Professional Hairdresser needs powerful, clever, simple, modern business card

I need a professional, clever, powerful, bold, attractive, modern/simplistic business card.
I specialize in dimensional hair color, precision haircutting, modern classic design, and signature finishes.
I believe in advanced education, continued training with emphasis on perfect practice, and strive to be the best at what I do.
I am trained by the industry's best and have passion for what I do, I want my business card to reflect my talents, education, capabilities, signature color techniques and design and confidence.
I want to be known as reputable, bold, artistic, aware, classic yet modern, innovative, creative, dimensional, knowledgeable, and educated.
I want something bold, simple, elegant, modern, clever, and legible.
My personal style is progressive, modern, eclectic, clean with modern luxury comfort style.
I love the use of black and white, to creative visual interest and texture. I think putting black as a solid background with white bold font makes the words jump/glow to the eye. I also think a stark white background with bold black fonts looks great, maybe with a punch of red. It is simple, clean, elegant.
I have a QR code I would like to include on the card but have no idea how to make it visually pleasing or make sense.
I do not have a set logo and am not sure if this needs to be done first or if the business card should be done first.

Target Market(s)

Early 20's-mid 60's, female and male, fashion aware, people who can afford my prices, appreciate value

Industry/Entity Type

Training

Requirements
Must have
• I would like to incorporate the QR code I have if possible.
I would like to have my name and contact info.
I would like my logo (or maybe have my logo be RT in a font like listed below).
I would like the fonts to be modern, bold, clean, readable.
Fonts I have looked at are: The font used on the book called: Vexaro A Hundred Years of Hue" I really love. I have looked at glyphvault.example for font and found "Georgiquas", but the designer wanted 200 euros which I just dont have at the time. Others I looked at include "Lin Libertine", Alien-Encounters-solid-regular-italic".
I love font used in the picture I included with the Tobin.Ashcroft ad.
Clean, modern, professional, legible, structured.
Nice to have
• I envision a black background with bold, modern, simple, font in white creating the effect of the words jumping off the card, visually apparent and glowing. Like a really expensive restaurant with a sign that you cant miss because the name is in bright white on black background, simple, bold, modern but not futuristic, powerful, clever, elegant, and draws the eye making it unforgetable. Perhaps layering black and white in order to where the font will be in white.
I see balance and chic.
Perhaps
Should not have
• I appreciate the trends in business design, but realize trends come and go and not sure if having something "trendy" is advisable for me. Having said that, I like creative modern design and sometimes current trends are important in design. I do like red as accent color, the primary blue color, blue on the PixelForum page, the masculine/florescent purple, and the neo bold yellow and the primary color shade of yellow.
I do not want clutter.
I do not want any fonts that are swirly, old-world calligraphy, script, or penmanship style.
I do not want picture of scissors, heads of old-school beauty school hair, or barber poles.

```html
<!DOCTYPE html>
<html lang="en">
<head>
<meta charset="utf-8">
<title>Remy Tallis Salon – Business Card</title>
<link href="https://fonts.googleapis.com/css2?family=Advent+Pro:wght@300;400&family=Syncopate:wght@700&display=swap" rel="stylesheet">
<style>
  :root {
    --bg-top: #272727;
    --bg-bottom: #16151a;
    --mint: #7ef2cc;
    --band: #3b3e42;
    --name-white: #f1f1ee;
    --periwinkle: #6d72bf;
    --city: #7b83d2;
    --phone-blue: #3b2fe6;
    --phone-red: #c4163f;
    --mark-magenta: #e01fc8;
    --mark-orange: #f27a12;
    --mark-navy: #0d1a4a;
  }
  * { margin: 0; padding: 0; box-sizing: border-box; }
  html, body {
    width: 714px;
    height: 1200px;
    overflow: hidden;
    background: var(--bg-bottom);
  }
  .card {
    position: relative;
    width: 714px;
    height: 1200px;
    overflow: hidden;
    background: linear-gradient(180deg, var(--bg-top) 0%, #1f1f21 45%, var(--bg-bottom) 100%);
    font-family: "Advent Pro", sans-serif;
  }
  .tagline {
    position: absolute;
    left: 26px;
    top: 74px;
    color: var(--mint);
    font-weight: 300;
    font-size: 54px;
    line-height: 58px;
    letter-spacing: 1px;
  }
  .brand-mark {
    position: absolute;
    left: 357px;
    top: 79px;
    width: 324px;
    height: 377px;
    border-radius: 0 60% 40% 40%;
    background:
      radial-gradient(ellipse at 30% 80%, rgba(224, 31, 200, 0.45) 0%, rgba(242, 122, 18, 0.25) 30%, transparent 60%),
      radial-gradient(ellipse at 75% 20%, rgba(13, 26, 74, 0.8) 0%, transparent 65%);
  }
  .name-band {
    position: absolute;
    left: 0;
    top: 529px;
    width: 714px;
    height: 63px;
    background: linear-gradient(180deg, #44474b 0%, var(--band) 50%, #34373a 100%);
  }
  .name-band svg { display: block; }
  .name-text {
    font-family: "Syncopate", sans-serif;
    font-weight: 700;
    font-size: 52px;
    fill: var(--name-white);
  }
  .salon {
    position: absolute;
    left: 103px;
    top: 668px;
    color: var(--periwinkle);
    font-weight: 300;
    font-size: 50px;
    letter-spacing: 30px;
  }
  .phone {
    position: absolute;
    left: 44px;
    top: 806px;
    color: var(--phone-blue);
    font-weight: 400;
    font-size: 116px;
    letter-spacing: 1px;
    text-shadow: 5px 0 0 var(--phone-red);
    white-space: nowrap;
  }
  .cities {
    position: absolute;
    top: 1096px;
    left: 0;
    width: 714px;
    height: 60px;
    color: var(--city);
    font-weight: 300;
    font-size: 58px;
    letter-spacing: 2px;
  }
  .city { position: absolute; top: 0; }
  .city-orlando { left: 18px; }
  .city-miami { left: 322px; }
  .city-milan { left: 541px; }
</style>
</head>
<body>
  <main class="card">
    <p class="tagline">color<br>is life</p>

    <div class="brand-mark" role="img" aria-label="Salon brand mark: a curved navy arc over a magenta and orange swoosh"></div>

    <div class="name-band">
      <svg width="714" height="63" viewBox="0 0 714 63">
        <text class="name-text" x="6" y="52" textLength="700" lengthAdjust="spacingAndGlyphs">REMY TALLIS</text>
      </svg>
    </div>

    <p class="salon">SALON</p>

    <p class="phone">421 558-3094</p>

    <div class="cities">
      <span class="city city-orlando">ORLANDO</span>
      <span class="city city-miami">MIAMI</span>
      <span class="city city-milan">MILAN</span>
    </div>
  </main>
</body>
</html>
```